Brisa Vale residential and commercial cleaning

We need a Business card design for a new residential and commercial cleaning company based in UAE- Abu Dhabi named (BRISA VALE)
we provide a residential cleaning service based in hourly rate (Maid Rent - Baby Setting), Also a commercial and offices cleaning.
Our logo is attached for your reference

Target Market(s)

Women who are 22 to 60 years old.

Industry/Entity Type

Residential

Requirements
Should not have
• it should not have an old-style fonts

```html
<!DOCTYPE html>
<html lang="en">
<head>
<meta charset="utf-8">
<title>Brisa Vale – Business Card</title>
<link rel="stylesheet" href="https://fonts.googleapis.com/css2?family=Source+Sans+3:wght@400;600;700&display=swap">
<style>
  :root {
    --canvas-bg: #e9e9ec;
    --card-bg: #ffffff;
    --brand-blue: #1a6fb0;
    --brand-green: #8cc63f;
    --ink: #111111;
    --band-text: #ffffff;
  }
  * { margin: 0; padding: 0; box-sizing: border-box; }
  html, body { width: 1200px; height: 1000px; overflow: hidden; }
  body {
    background: var(--canvas-bg);
    font-family: "Source Sans 3", Arial, sans-serif;
    color: var(--ink);
    position: relative;
  }
  .card {
    position: absolute;
    left: 265px;
    width: 666px;
    height: 397px;
    background: var(--card-bg);
    box-shadow: 0 2px 10px rgba(0,0,0,0.18);
    overflow: hidden;
  }
  .card--front { top: 73px; }
  .card--back { top: 533px; }

  .wordmark {
    display: flex;
    align-items: center;
    gap: 14px;
    color: var(--brand-blue);
    font-weight: 700;
    white-space: nowrap;
  }
  .wordmark__dot {
    border-radius: 50%;
    background: var(--brand-green);
    flex: none;
  }
  .card--front .wordmark {
    position: absolute;
    left: 0; right: 0; top: 0; bottom: 0;
    justify-content: center;
    font-size: 82px;
  }
  .card--front .wordmark__dot { width: 58px; height: 58px; }

  .card--back .wordmark {
    position: absolute;
    left: 25px; top: 70px;
    font-size: 38px;
    gap: 10px;
  }
  .card--back .wordmark__dot { width: 26px; height: 26px; }

  .availability {
    position: absolute;
    left: 24px; top: 180px;
    font-size: 18.5px;
    font-weight: 700;
  }
  .contact-list {
    position: absolute;
    left: 24px; top: 222px;
    list-style: none;
  }
  .contact-list li {
    display: flex;
    align-items: center;
    gap: 8px;
    font-size: 17.5px;
    height: 29.5px;
  }
  .contact-list svg { width: 14px; height: 16px; flex: none; }

  .services {
    position: absolute;
    left: 379px; top: 46px;
  }
  .services__title {
    font-size: 18.5px;
    font-weight: 700;
    margin-bottom: 14px;
  }
  .services__list { list-style: none; }
  .services__list li {
    font-size: 17.5px;
    height: 38px;
  }

  .tagline-band {
    position: absolute;
    left: 0; right: 0; bottom: 0;
    height: 36px;
    background: var(--brand-blue);
    display: flex;
    align-items: center;
    justify-content: space-between;
    padding: 0 42px 0 44px;
    color: var(--band-text);
  }
  .tagline-band__dot {
    width: 9px; height: 9px;
    border-radius: 50%;
    background: var(--band-text);
  }
  .tagline-band__text {
    font-size: 18px;
    letter-spacing: 4.2px;
  }
</style>
</head>
<body>

  <section class="card card--front" aria-label="Business card front">
    <div class="wordmark">
      <span>Brisa Vale</span>
      <span class="wordmark__dot"></span>
    </div>
  </section>

  <section class="card card--back" aria-label="Business card back">
    <div class="wordmark">
      <span>Brisa Vale</span>
      <span class="wordmark__dot"></span>
    </div>

    <p class="availability">Same Day Appointment Available !</p>

    <ul class="contact-list">
      <li>
        <svg viewBox="0 0 14 16" aria-hidden="true"><circle cx="7" cy="4.5" r="3.5" fill="#8cc63f"/><path d="M0 16c0-4.5 3-7 7-7s7 2.5 7 7z" fill="#8cc63f"/></svg>
        Lina Harmon
      </li>
      <li>
        <svg viewBox="0 0 14 16" aria-hidden="true"><rect x="3.5" y="1" width="7" height="14" rx="1.5" fill="#8cc63f"/><rect x="5" y="3" width="4" height="6" fill="#fff"/></svg>
        Call / Text &nbsp;(702) 555 - 0148
      </li>
      <li>
        <svg viewBox="0 0 14 16" aria-hidden="true"><path d="M1 6c0-2 3-3 6-3s6 1 6 3l-2 1-1-2H4L3 7z" fill="#8cc63f"/><rect x="2.5" y="8" width="9" height="6" rx="1" fill="#8cc63f"/></svg>
        Office (902) 555 - 0192
      </li>
      <li>
        <svg viewBox="0 0 14 16" aria-hidden="true"><circle cx="7" cy="8" r="6" fill="#8cc63f"/><path d="M1 8h12M7 2v12M3 4.5h8M3 11.5h8" stroke="#fff" stroke-width="0.9" fill="none"/></svg>
        P.O. Box 48210 Abu Dhabi, UAE
      </li>
    </ul>

    <div class="services">
      <h2 class="services__title">Residential &amp; Commercial</h2>
      <ul class="services__list">
        <li>- Baby Sitting</li>
        <li>- Maid Rent</li>
        <li>- Area Rugs</li>
        <li>- Steam Carpet Care</li>
        <li>- Upholstery</li>
        <li>- Air Duct Cleaning</li>
        <li>- Tile &nbsp;&amp; &nbsp;Grout Cleaning</li>
      </ul>
    </div>

    <div class="tagline-band">
      <span class="tagline-band__dot"></span>
      <span class="tagline-band__text">Cleaner &nbsp;&amp; &nbsp;Healthier Indoor Environments</span>
      <span class="tagline-band__dot"></span>
    </div>
  </section>

</body>
</html>
```